New Body Mist 250 ml exclusive

We are excited to embark on a new project to design the packaging for body mist:
Lunar Bramble

We are looking for a design that is truly unique and stands out, with a touch of individuality that sets it apart. The design should be eye-catching and visually appealing, drawing attention even from a distance. We want the body mists to have a fun and attractive look that appeals to customers.

To help bring your design to life, we will provide the dimensions of the bottle, which has a capacity of 250ml. The bottle measures 13.3 cm in height and 4.9 cm in diameter (excluding the pump). Additionally, we will also provide the dimensions of the label, which measures 15.1 cm in height and 12.8 cm in width.

We believe that giving you the freedom to put your own unique touch and color choices will help create a truly standout design. We look forward to seeing your creative vision for our body mist.

We shared with you the logo of the body mist and some examples of models that we liked.

Please be informed that the project only includes one design and the remaining three will be completed and paid for through a 1on1 project with the winner of the contest.

Target Market(s)

Supermarket and perfumery stores

Industry/Entity Type

Cosmetics

Font styles to use
Serif

Requirements
Must have
• Uniqueness and attractiveness

```html
<!DOCTYPE html>
<html lang="en">
<head>
<meta charset="utf-8">
<title>Lunar Bramble – Velvet Dew Body Mist Label</title>
<link rel="stylesheet" href="https://fonts.googleapis.com/css2?family=Josefin+Sans:wght@400;600&family=Mrs+Saint+Delafield&family=Roboto:wght@400;500&display=swap">
<style>
  :root {
    --page: #ece8e9;
    --mint: #c6efdf;
    --pearl: #f8f0f3;
    --blush: #f4cfdb;
    --rose: #ec9db2;
    --ink: #6a1e30;
    --brand-ink: #2e2428;
    --pill: #7a2233;
    --pill-text: #ffffff;
    --volume-ink: #1f1a1c;
  }
  * { box-sizing: border-box; margin: 0; padding: 0; }
  html, body { width: 1200px; height: 1200px; overflow: hidden; }
  body {
    background: var(--page);
    display: flex;
    align-items: center;
    justify-content: center;
  }
  .label {
    position: relative;
    width: 780px;
    height: 920px;
    overflow: hidden;
    box-shadow: 0 10px 40px rgba(60, 20, 35, 0.18);
  }
  .label__artwork {
    position: absolute;
    inset: 0;
    background: linear-gradient(180deg, var(--mint) 0%, var(--pearl) 32%, var(--blush) 68%, var(--rose) 100%);
  }
  .label__front {
    position: absolute;
    inset: 0;
    display: flex;
    flex-direction: column;
    align-items: center;
  }
  .brand-name {
    margin-top: 148px;
    font-family: "Josefin Sans", sans-serif;
    font-weight: 600;
    font-size: 34px;
    letter-spacing: 0.12em;
    font-variant: small-caps;
    color: var(--brand-ink);
  }
  .product-name {
    margin-top: 90px;
    font-family: "Mrs Saint Delafield", cursive;
    font-weight: 400;
    font-size: 140px;
    line-height: 0.85;
    color: var(--ink);
    text-align: center;
    transform: rotate(-12deg);
  }
  .product-name span { display: block; }
  .product-name span + span { margin-left: 70px; }
  .product-type {
    margin-top: 130px;
    padding: 6px 22px 5px;
    background: var(--pill);
    color: var(--pill-text);
    font-family: "Roboto", sans-serif;
    font-weight: 500;
    font-size: 22px;
    letter-spacing: 0.22em;
  }
  .volume {
    position: absolute;
    bottom: 62px;
    font-family: "Roboto", sans-serif;
    font-size: 30px;
    color: var(--volume-ink);
  }
</style>
</head>
<body>
  <main class="label">
    <div class="label__artwork" role="img" aria-label="Marbled alcohol-ink artwork in mint green, blush pink, crimson and plum with gold flecks"></div>

    <section class="label__front">
      <p class="brand-name">Lunar Bramble</p>
      <h1 class="product-name"><span>Velvet</span><span>Dew</span></h1>
      <p class="product-type">BODY MIST</p>
      <p class="volume">250 ml</p>
    </section>
  </main>
</body>
</html>
```